VelmoraHub

Hey

I am involved with crowd funding, please look at one of my current sites www.funsprell.com
Work is currently under way with a new site www.velmorahub.com .wehave the basics but I am not happy with what we have so far. I need to redesign the web site but keep the concept . The cartoon pitch will be kept , along with some of the other functions which we can help you with, unless you are able to build / design something better. I liked a lot of the designs submitted for a previous crowd funning design, far better than what I currently have. To be included on this site will be links to numerous crowd funding sites which I have registered but each site will be focused on a specific topic which will be disclosed once this site is active. I intend to build all these sites through this site. Along with these sites will be a logo design for each site so plenty of work going forward. I have a logo for velmorahub already but am open for improvements and suggestions but would like to keep a map or logo of Africa included in the design. To bear in mind this is a African focused buisness which aims to help communities, employment creation, poverty alleviation and help young entrepreneurs kickstarter their buisness . I already have a group logo , which was designed on this site ( look at tandel yards competition) , I would like this logo to be used on all the site so customers and investors link the group and concept togeather. Here is the link http://www.brievoshop.co.uk/project-progress.aspx?briefId=48213 . I have removed the tandelyard from the bottom of the logo and will just be using the figurines as the group logo on all web sites. There will be at least fifty related crowd fund projects linked to this site.
If any body has any questions or ideas please feel free to ask for anything you may need. Thanks to everybody who helps with this project. Warmly. Ravi

Hi everyone working on my design.

The contact details to use on the site are

27 Weltmore Close
Dunvale
Cape Town 
+263748395026
+447913462058

E mail enquiries@VelmoraHub.example

There are two logos, one is the velmorahub logo and the other is my group logo which I will attach to the pitch
Good luck and thank you to everybody who is working on this web design
Warmly

Ravi

```html
<!DOCTYPE html>
<html lang="en">
<head>
<meta charset="utf-8">
<title>VelmoraHub – Equity Crowdfunding</title>
<link href="https://fonts.googleapis.com/css2?family=Arimo:wght@400;700&family=Oswald:wght@400&family=PT+Serif&display=swap" rel="stylesheet">
<style>
:root{
  --dark:#2c2c2c;
  --darker:#1f1f1f;
  --page:#ebebeb;
  --header:#f4f4f4;
  --blue:#1a8ad0;
  --blue-deep:#0b6aa9;
  --link-blue:#1a86c9;
  --green:#8cb82a;
  --green-box:#6cb33f;
  --blue-box:#1a9ad9;
  --text:#333;
  --muted:#666;
  --line:#d6d6d6;
  --white:#fff;
}
*{box-sizing:border-box;margin:0;padding:0}
html,body{width:976px;height:1200px;overflow:hidden;background:var(--page)}
body{font-family:"Arimo",Arial,sans-serif;color:var(--text);font-size:10px}
.canvas{position:relative;width:976px;height:1200px;overflow:hidden;background:var(--page)}
.abs{position:absolute}
a{color:inherit;text-decoration:none}

/* top bar */
.topbar{left:0;top:0;width:976px;height:27px;background:var(--dark)}
.topbar .mid{position:absolute;left:359px;top:0;width:170px;height:27px;background:#3a3a3a}
.topbar .links{position:absolute;left:359px;top:9px;width:170px;text-align:center;color:#ddd;font-size:8px;white-space:nowrap}
.topbar .links span{margin:0 2px}
.topbar .account{position:absolute;left:571px;top:9px;color:#eee;font-size:8px;white-space:nowrap;display:flex;gap:16px}
.topbar .account .reg{display:flex;gap:6px;font-weight:700}

/* header */
.header{left:0;top:27px;width:976px;height:85px;background:var(--header)}
.brand{left:186px;top:46px;display:flex;align-items:center;gap:8px}
.brand .dot{width:34px;height:34px;border-radius:50%;background:var(--green)}
.brand .name{font-size:25px;font-weight:700;color:var(--blue-deep);letter-spacing:-.5px}
.brand-tag{left:270px;top:76px;font-size:6.5px;font-weight:700;color:#333;letter-spacing:.3px}
.btn{position:absolute;height:20px;border-radius:3px;color:#fff;font-size:8.5px;font-weight:700;display:flex;align-items:center;justify-content:center;white-space:nowrap}
.btn-social{left:480px;top:36px;width:116px;background:linear-gradient(#5573b0,#3b5998)}
.btn-social i{display:block;width:13px;height:13px;background:#2b4580;margin-right:7px;border-radius:2px}
.btn-signup{left:604px;top:36px;width:70px;background:linear-gradient(#a6c45a,#7fa031)}
.btn-login{left:680px;top:36px;width:108px;background:linear-gradient(#a6c45a,#7fa031)}
.phone-icon{left:690px;top:64px;width:20px;height:20px;border-radius:50%;background:var(--link-blue)}
.phones{left:716px;top:65px;font-size:9px;line-height:12px;letter-spacing:.5px}
.mail{left:660px;top:92px;font-size:9px;display:flex;align-items:center;gap:6px}

/* nav */
.nav{left:0;top:112px;width:976px;height:29px;background:linear-gradient(var(--blue),var(--blue-deep))}
.nav ul{position:absolute;left:184px;top:8px;list-style:none;display:flex;color:#fff;font-size:10px;font-weight:700}
.nav li{padding:0 5px;border-left:1px solid #7cc0ea}
.nav li:first-child{padding-left:0;border-left:0}
.search{left:634px;top:117px;width:154px;height:19px;background:#fff;border-radius:3px;font-size:9px;color:#555;padding:4px 8px}
.search .go{position:absolute;right:0;top:0;width:20px;height:19px;background:#e6e6e6;border-radius:0 3px 3px 0}

/* slider */
.slider{left:182px;top:146px;width:610px;height:180px;background:#fff;border:1px solid #ddd;box-shadow:0 2px 4px rgba(0,0,0,.1)}
.slider .photo{position:absolute;left:5px;top:5px;width:598px;height:123px;background:linear-gradient(180deg,#b7a7a8 0%,#6e6a79 45%,#3a3c4c 100%)}
.slider .caption{position:absolute;left:20px;top:136px;width:570px;text-align:center;font-family:"PT Serif",Georgia,serif;font-size:11px;line-height:13px;color:#555}
.arrow{position:absolute;top:288px;width:20px;height:24px;background:#444;color:#fff;font-size:10px;display:flex;align-items:center;justify-content:center}
.arrow.left{left:166px;border-radius:12px 0 0 12px}
.arrow.right{left:790px;border-radius:0 12px 12px 0}

/* welcome */
.welcome-title{left:182px;top:344px;font-size:12px;font-weight:700;color:var(--link-blue)}
.band{left:0;top:368px;width:976px;height:180px;background:#f6f6f6;border-top:1px solid #ddd;border-bottom:1px solid #ddd}
.what{left:198px;top:386px;width:282px}
.what h2{font-size:15.5px;font-weight:700;color:#222;margin-bottom:10px}
.what p{font-size:10.6px;line-height:13px;color:#555}
.what p b{color:var(--link-blue)}
.pill{position:absolute;top:494px;height:20px;border-radius:10px;font-size:8.5px;font-weight:700;display:flex;align-items:center;justify-content:center}
.pill-light{left:202px;width:76px;background:#d8eef8;color:#3a8dc4;border:1px solid #b5d8ec}
.pill-blue{left:286px;width:76px;background:linear-gradient(#3d90d7,#1563a8);color:#fff}
.video{left:482px;top:343px;width:301px;height:195px;background:#111;border-radius:2px}
.video .frame{position:absolute;left:3px;top:5px;width:295px;height:178px;background:linear-gradient(135deg,#bdbdbd,#8e8e8e)}
.video .play{position:absolute;left:138px;top:78px;width:28px;height:22px;background:rgba(0,0,0,.7);border-radius:3px}
.video .bar{position:absolute;left:4px;top:186px;width:292px;height:4px;background:#444}

/* cards */
.card{position:absolute;top:555px;width:150px;height:219px;background:#fff;border:1px solid #d0d0d0;border-radius:3px;overflow:hidden}
.card .tab{height:27px;background:linear-gradient(#eaf4fa,#d5e8f2);border-bottom:1px solid #cfe2ec;text-align:center;font-size:8.8px;padding-top:9px;color:#333;white-space:nowrap}
.card h3{position:absolute;left:9px;top:38px;font-size:8.8px;color:var(--link-blue);white-space:nowrap}
.card p{position:absolute;left:9px;top:56px;width:130px;height:53px;overflow:hidden;font-size:8.6px;line-height:10.5px;text-align:justify;color:#333}
.card .more{position:absolute;right:9px;top:111px;width:34px;height:12px;background:#eee;border:1px solid #ccc;font-size:7.5px;text-align:center;line-height:10px}
.card .stats{position:absolute;left:0;top:128px;width:148px;height:89px;border-top:1px solid #e4e4e4}
.card .count{position:absolute;left:8px;top:8px;display:flex;align-items:center;gap:10px;font-size:14px}
.card .row{position:absolute;left:8px;width:132px;font-size:9px;border-top:1px solid #eee;padding-top:7px}
.card .row b{color:var(--green);display:inline-block;width:40px}
.card .row.r1{top:36px}
.card .row.r2{top:60px}

/* categories */
.cat-title{left:182px;top:792px;font-size:12px;font-weight:700;color:var(--link-blue)}
.cat-rule{left:182px;top:812px;width:216px;height:2px;background:#c9c9c9}
.cat-rule span{display:block;width:90px;height:2px;background:var(--link-blue)}
.cats{position:absolute;top:828px;width:110px;list-style:none}
.cats li{font-size:9.5px;color:#555;padding:3px 0 3px 5px;border-left:2px solid var(--link-blue);border-bottom:1px solid #ddd;margin-bottom:3px;height:16px;white-space:nowrap}
.cats li.on{color:var(--green);font-weight:700}
.cta{position:absolute;top:797px;width:148px;height:133px;color:#fff;padding:10px}
.cta h4{font-family:"Oswald","Arial Narrow",sans-serif;font-weight:400;font-size:19px;margin-bottom:6px}
.cta p{position:relative;z-index:1;font-size:9.2px;line-height:11px;text-align:justify}
.cta .art{position:absolute;right:8px;bottom:0;width:70px;height:40px;background:rgba(255,255,255,.25)}
.cta-join{left:490px;background:var(--blue-box)}
.cta-fund{left:644px;background:var(--green-box)}

/* footer */
.footer-edge{left:0;top:962px;width:976px;height:6px;background:repeating-linear-gradient(45deg,#ccc 0 2px,#e2e2e2 2px 4px)}
.footer{left:0;top:968px;width:976px;height:202px;background:var(--dark);color:#ddd}
.footer h5{position:absolute;top:22px;font-size:11px;color:#fff}
.flinks{position:absolute;top:48px;list-style:none;width:82px}
.flinks li{font-size:9px;padding:4px 0;border-bottom:1px solid #444;height:20px}
.contact{position:absolute;left:388px;top:48px;width:176px;list-style:none}
.contact li{font-size:9px;padding:4px 0;border-bottom:1px solid #444;height:20px;white-space:nowrap}
.field{position:absolute;left:591px;width:202px;height:18px;background:#fff;color:#444;font-size:8.5px;padding:4px 12px}
.submit{left:718px;top:1099px;width:74px;height:20px;background:linear-gradient(#eef8fc,#c9e3ee);border-radius:10px;color:#2b7cae;font-size:9px;text-align:center;line-height:20px}
.badge{position:absolute;top:1124px;height:30px}
.b1{left:182px;width:120px;background:#4d7d25;border-radius:15px 3px 3px 15px}
.b2{left:314px;width:78px;background:#e4e4e4;border-radius:2px}
.b3{left:410px;width:62px;background:#f3c419;border-radius:15px}
.social{position:absolute;top:1133px;width:18px;height:18px;border-radius:2px}
.copy{left:0;top:1170px;width:976px;height:30px;background:#f2f2f2;text-align:center;font-size:8.5px;line-height:30px;color:#444}
.copy a{color:var(--link-blue)}
</style>
</head>
<body>
<div class="canvas">

  <div class="abs topbar">
    <div class="mid"></div>
    <div class="links"><span>Blogs</span>|<span>IPO's</span>|<span>How it Works</span>|<span>About VelmoraHub</span></div>
    <div class="account"><span>Welcome Guest!</span><span>My Account</span><span>Wishlist</span><span class="reg"><span>| Register</span><span>Sign In</span></span></div>
  </div>

  <div class="abs header"></div>
  <div class="abs brand"><span class="dot"></span><span class="name">VelmoraHub</span></div>
  <div class="abs brand-tag">EQUITY CROWDFUNDING</div>
  <div class="btn btn-social"><i></i>Sign in with Linkora</div>
  <div class="btn btn-signup">Sign Up Today</div>
  <div class="btn btn-login">Login to your Account</div>
  <svg class="abs phone-icon" viewBox="0 0 20 20" aria-hidden="true"><path d="M7 5l2 2-1 1.5c.8 1.6 2 2.8 3.5 3.5L13 11l2 2-1.5 2C9 14.5 5.5 11 5 6.5z" fill="#fff"/></svg>
  <div class="abs phones">+263748395026<br>+447913462058</div>
  <div class="abs mail"><svg width="14" height="9" viewBox="0 0 14 9" aria-hidden="true"><rect x=".5" y=".5" width="13" height="8" fill="none" stroke="#555"/><path d="M.5.5L7 5l6.5-4.5" fill="none" stroke="#555"/></svg>enquiries@VelmoraHub.example</div>

  <nav class="abs nav">
    <ul><li>Home</li><li>Company Info</li><li>Join Now!</li><li>How it works?</li><li>Browse Companies</li></ul>
  </nav>
  <div class="abs search">search...<span class="go"></span></div>

  <section class="abs slider">
    <div class="photo" role="img" aria-label="Group photo of business people standing together"></div>
    <p class="caption">Ground rules are simple; JOIN, send us a Vidzo or any other video link to any idea. It can be an idea just floating around or an idea which has already come to life. No catches, no entry fee, no award collection fee, only one entry per member.</p>
  </section>
  <div class="arrow left">&#9664;</div>
  <div class="arrow right">&#9654;</div>

  <h1 class="abs welcome-title">Welcome to Africa's leading crowdfunding site</h1>
  <div class="abs band"></div>
  <div class="abs what">
    <h2>What is Crowdfunding?</h2>
    <p>Crowdfunding enables people to raise money for innovative new projects by getting like-minded individuals to pool their money to back the idea, person or business. It's a way to make things happen. <b>WATCH THE VIDEO</b></p>
  </div>
  <div class="pill pill-light">Learn more here</div>
  <div class="pill pill-blue">Join Now!</div>
  <div class="abs video">
    <div class="frame" role="img" aria-label="Cartoon pitch video explaining crowdfunding"></div>
    <div class="play"></div>
    <div class="bar"></div>
  </div>

  <div class="card" style="left:182px">
    <div class="tab">Russia</div>
    <h3>Lorem ipsum dolor sit amet,</h3>
    <p>Adipiscing elit. Curabitur eu interdum dui. Aliquam turpis mauris, rhoncus et tempus ac, pellentesque quis sem. Nullam a leo arcu, in posuere leo.</p>
    <div class="more">more</div>
    <div class="stats">
      <div class="count"><svg width="26" height="14" viewBox="0 0 26 14" aria-hidden="true"><g fill="#8cb82a"><circle cx="6" cy="4" r="3"/><circle cx="13" cy="3.5" r="3.3"/><circle cx="20" cy="4" r="3"/><rect x="1" y="8" width="10" height="6" rx="3"/><rect x="8" y="7.5" width="10" height="6.5" rx="3"/><rect x="15" y="8" width="10" height="6" rx="3"/></g></svg>0</div>
      <div class="row r1"><b>Funded</b>$0.00</div>
      <div class="row r2"><b>Goal</b>$3000.00</div>
    </div>
  </div>
  <div class="card" style="left:337px">
    <div class="tab">Middle East</div>
    <h3>Lorem ipsum dolor sit amet,</h3>
    <p>Adipiscing elit. Curabitur eu interdum dui. Aliquam turpis mauris, rhoncus et tempus ac, pellentesque quis sem. Nullam a leo arcu, in posuere leo.</p>
    <div class="more">more</div>
    <div class="stats">
      <div class="count"><svg width="26" height="14" viewBox="0 0 26 14" aria-hidden="true"><g fill="#8cb82a"><circle cx="6" cy="4" r="3"/><circle cx="13" cy="3.5" r="3.3"/><circle cx="20" cy="4" r="3"/><rect x="1" y="8" width="10" height="6" rx="3"/><rect x="8" y="7.5" width="10" height="6.5" rx="3"/><rect x="15" y="8" width="10" height="6" rx="3"/></g></svg>0</div>
      <div class="row r1"><b>Funded</b>$0.00</div>
      <div class="row r2"><b>Goal</b>$3000.00</div>
    </div>
  </div>
  <div class="card" style="left:490px">
    <div class="tab">Eastern Europe</div>
    <h3>Lorem ipsum dolor sit amet,</h3>
    <p>Adipiscing elit. Curabitur eu interdum dui. Aliquam turpis mauris, rhoncus et tempus ac, pellentesque quis sem. Nullam a leo arcu, in posuere leo.</p>
    <div class="more">more</div>
    <div class="stats">
      <div class="count"><svg width="26" height="14" viewBox="0 0 26 14" aria-hidden="true"><g fill="#8cb82a"><circle cx="6" cy="4" r="3"/><circle cx="13" cy="3.5" r="3.3"/><circle cx="20" cy="4" r="3"/><rect x="1" y="8" width="10" height="6" rx="3"/><rect x="8" y="7.5" width="10" height="6.5" rx="3"/><rect x="15" y="8" width="10" height="6" rx="3"/></g></svg>0</div>
      <div class="row r1"><b>Funded</b>$0.00</div>
      <div class="row r2"><b>Goal</b>$3000.00</div>
    </div>
  </div>
  <div class="card" style="left:643px">
    <div class="tab">Gache Gache Reserve, Zimbabwe</div>
    <h3>Lorem ipsum dolor sit amet,</h3>
    <p>Adipiscing elit. Curabitur eu interdum dui. Aliquam turpis mauris, rhoncus et tempus ac, pellentesque quis sem. Nullam a leo arcu, in posuere leo.</p>
    <div class="more">more</div>
    <div class="stats">
      <div class="count"><svg width="26" height="14" viewBox="0 0 26 14" aria-hidden="true"><g fill="#8cb82a"><circle cx="6" cy="4" r="3"/><circle cx="13" cy="3.5" r="3.3"/><circle cx="20" cy="4" r="3"/><rect x="1" y="8" width="10" height="6" rx="3"/><rect x="8" y="7.5" width="10" height="6.5" rx="3"/><rect x="15" y="8" width="10" height="6" rx="3"/></g></svg>5</div>
      <div class="row r1"><b>Funded</b>$5.00</div>
      <div class="row r2"><b>Goal</b>$100.00</div>
    </div>
  </div>

  <h2 class="abs cat-title">Business Categories</h2>
  <div class="abs cat-rule"><span></span></div>
  <ul class="cats" style="left:184px">
    <li>Comics</li><li>Environment</li><li>Fashion</li><li>Film &amp; Video</li><li>Gaming</li><li>Health &amp; Fitness</li>
  </ul>
  <ul class="cats" style="left:322px">
    <li>Music</li><li>Professional Services</li><li>Technology</li><li>More links</li><li class="on">Internet &amp; IT</li><li>Leasure &amp; Tourism</li>
  </ul>

  <div class="cta cta-join">
    <h4>JOIN NOW!</h4>
    <p>Adipiscing elit. Curabitur eu interdum dui. Aliquam turpis mauris, rhoncus et tempus ac, pellentesque quis sem. Nullam a leo arcu, in posuere leo.</p>
    <div class="art" role="img" aria-label="Silhouettes of two members"></div>
  </div>
  <div class="cta cta-fund">
    <h4>FUND</h4>
    <p>Adipiscing elit. Curabitur eu interdum dui. Aliquam turpis mauris, rhoncus et tempus ac, pellentesque quis sem. Nullam a leo arcu, in posuere leo.</p>
    <div class="art" role="img" aria-label="Price tag with dollar sign"></div>
  </div>

  <div class="abs footer-edge"></div>
  <footer class="abs footer">
    <h5 style="left:185px">About Us</h5>
    <ul class="flinks" style="left:185px"><li>About US</li><li>Join Now</li><li>How it works</li><li>Privacy policy</li><li>Our Blog</li></ul>
    <ul class="flinks" style="left:266px"><li>Resources</li><li>FAQ</li><li>Email Us</li><li>My Account</li><li>Sign Up now</li></ul>
    <h5 style="left:388px">Contact Us</h5>
    <ul class="contact"><li>Phone: +263748395026</li><li>Fax: &nbsp; +447913462058</li><li>enquiries@VelmoraHub.example</li><li>27 Weltmore Close, Dunvale, Cape Town</li></ul>
    <h5 style="left:591px">Comments &amp; Feedback</h5>
  </footer>
  <div class="field" style="top:1012px">Enter your name</div>
  <div class="field" style="top:1033px">Enter your email here</div>
  <div class="field" style="top:1055px;height:35px">Message</div>
  <div class="abs submit">Submit</div>

  <div class="badge b1"></div>
  <div class="badge b2"></div>
  <div class="badge b3"></div>
  <div class="social" style="left:592px;background:#3b5998"></div>
  <div class="social" style="left:615px;background:#2aa9e0"></div>
  <div class="social" style="left:638px;background:#0e76a8"></div>
  <div class="social" style="left:661px;background:#cb2027"></div>
  <div class="social" style="left:684px;background:#d34836"></div>
  <div class="social" style="left:707px;background:#bdbdbd"></div>
  <div class="social" style="left:730px;background:#2bb673"></div>

  <div class="abs copy">Copyright 2012 VelmoraHub &nbsp; / &nbsp; Use of this website constitutes acceptance of our <a>User Agreement</a> and <a>Privacy Policy</a></div>
</div>
</body>
</html>
```